Stationery Design Project

We are a start up wine business based in Sydney Australia. We already have a logo and are in the process of completing our website. We require our logo to be cleverly and artfully incorporated into our stationary requirements. Which will initially begin with a company letter head.
As we desire consistency across our brand, we will also be wanting to develop banner advertisements and brochure with the same "look".
If outstanding we move design brief to banner advertisement for web and banner of the website itself.
Target Market(s)
Older wealthy predominantly male demographic
Industry/Entity Type
Business
Look and feel

```html
<!DOCTYPE html>
<html lang="en">
<head>
<meta charset="utf-8">
<title>Vintage Row Wines – Letterhead Options</title>
<link href="https://fonts.googleapis.com/css2?family=Arimo:wght@400&display=swap" rel="stylesheet">
<style>
  :root {
    --backdrop: #e7e3dd;
    --paper: #ffffff;
    --paper-shade: #f3f3f3;
    --ink: #1f1f1f;
    --band: #1a1a1a;
    --silver: #b9b9b9;
    --faint: #d9d9d9;
    --label: #3a3a3a;
    --on-band: #ffffff;
  }
  * { margin: 0; padding: 0; box-sizing: border-box; }
  html, body {
    width: 1200px; height: 817px; overflow: hidden;
    background: var(--backdrop);
    font-family: "Arimo", Arial, sans-serif;
  }
  .board { position: relative; width: 1200px; height: 817px; }

  .sheet {
    position: absolute; top: 48px; width: 538px; height: 698px;
    background: radial-gradient(ellipse at 50% 45%, var(--paper) 40%, var(--paper-shade) 100%);
    box-shadow: 0 2px 6px rgba(0,0,0,.25);
    overflow: hidden;
  }
  .sheet--one { left: 40px; }
  .sheet--two { left: 605px; }

  .brand-name {
    position: absolute; top: 96px; left: 0; width: 100%;
    text-align: center; color: var(--ink);
    font-size: 22px; line-height: 26px; font-weight: 400; letter-spacing: .5px;
  }

  .watermark-name {
    position: absolute; top: 395px; left: 0; width: 100%;
    text-align: center; color: var(--faint);
    font-size: 44px; line-height: 52px; font-weight: 400;
  }

  .footer-band { position: absolute; left: 0; bottom: 0; width: 538px; height: 90px; }
  .sheet--one .footer-band { height: 110px; }

  .contact-list { list-style: none; font-size: 9.5px; line-height: 11.5px; }
  .contact-list li { display: flex; align-items: center; gap: 4px; }
  .contact-list svg { width: 8px; height: 8px; flex: none; }

  .contact-list--band {
    position: absolute; right: 12px; bottom: 30px; color: var(--on-band);
    line-height: 11px;
  }
  .contact-list--band li { justify-content: flex-end; }
  .contact-list--band svg { fill: var(--on-band); }

  .contact-list--top {
    position: absolute; top: 68px; left: 412px;
    padding-left: 8px; border-left: 1px solid var(--silver); color: #333;
  }
  .contact-list--top svg { fill: #444; }

  .address {
    position: absolute; right: 12px; bottom: 12px;
    color: var(--on-band); font-size: 10.5px;
  }
  .sheet--two .address { right: 20px; bottom: 18px; }

  .option-label {
    position: absolute; top: 762px; width: 200px; text-align: center;
    color: var(--label); font-size: 19px;
  }
  .option-label--one { left: 209px; }
  .option-label--two { left: 774px; }
</style>
</head>
<body>
<main class="board">
  <svg width="0" height="0" style="position:absolute" aria-hidden="true">
    <defs>
      <linearGradient id="swoosh" x1="0" x2="1">
        <stop offset="0" stop-color="#444"/>
        <stop offset=".45" stop-color="#e6e6e6"/>
        <stop offset=".75" stop-color="#9a9a9a"/>
        <stop offset="1" stop-color="#f2f2f2"/>
      </linearGradient>
      <symbol id="icon-phone" viewBox="0 0 10 10"><path d="M2 1l2 2-1 1.2c.6 1.2 1.5 2.1 2.8 2.8L7 6l2 2-1.3 1.4C4.5 9 1 5.5.6 2.3z"/></symbol>
      <symbol id="icon-person" viewBox="0 0 10 10"><circle cx="5" cy="3" r="2.2"/><path d="M1 10c0-3 2-4.5 4-4.5S9 7 9 10z"/></symbol>
      <symbol id="icon-mail" viewBox="0 0 10 10"><rect x="0" y="2" width="10" height="6.5"/><path d="M0 2l5 3.5L10 2" stroke="#888" fill="none" stroke-width=".8"/></symbol>
      <symbol id="icon-globe" viewBox="0 0 10 10"><circle cx="5" cy="5" r="4.5"/><path d="M.5 5h9M5 .5v9" stroke="#888" stroke-width=".7"/></symbol>
    </defs>
  </svg>

  <section class="sheet sheet--one">
    <p class="brand-name">Vintage Row<br>Wines</p>

    <svg class="footer-band" viewBox="0 0 538 110" aria-hidden="true">
      <path d="M0 100 C180 100 300 16 538 12 L538 110 L0 110 Z" fill="var(--band)"/>
      <path d="M0 88 C180 94 300 4 538 0 L538 6 C300 10 180 100 0 95 Z" fill="url(#swoosh)"/>
    </svg>
    <ul class="contact-list contact-list--band">
      <li>123-555-0142 <svg><use href="#icon-phone"/></svg></li>
      <li>123-555-0142 <svg><use href="#icon-person"/></svg></li>
      <li>mail@vintagerow.com <svg><use href="#icon-mail"/></svg></li>
      <li>www.vintagerow.com <svg><use href="#icon-globe"/></svg></li>
    </ul>
    <p class="address">Street Name, City, State, zip code</p>
  </section>

  <section class="sheet sheet--two">
    <p class="brand-name">Vintage Row<br>Wines</p>

    <ul class="contact-list contact-list--top">
      <li><svg><use href="#icon-phone"/></svg> 123-555-0142</li>
      <li><svg><use href="#icon-person"/></svg> 123-555-0142</li>
      <li><svg><use href="#icon-mail"/></svg> mail@vintagerow.com</li>
      <li><svg><use href="#icon-globe"/></svg> www.vintagerow.com</li>
    </ul>

    <p class="watermark-name">Vintage Row<br>Wines</p>

    <svg class="footer-band" viewBox="0 0 538 90" aria-hidden="true">
      <path d="M0 84 C170 82 380 42 538 30 L538 90 L0 90 Z" fill="var(--band)"/>
      <path d="M0 72 C180 80 380 36 538 20 L538 26 C380 42 180 86 0 80 Z" fill="url(#swoosh)"/>
    </svg>
    <p class="address">Street Name, City, State, zip code</p>
  </section>

  <p class="option-label option-label--one">Option-1</p>
  <p class="option-label option-label--two">Option-2</p>
</main>
</body>
</html>
```